engaging mobile application to encourage lifestyle change

We need an App that will help people get from Bloom 4 Joy. A weight loss program based on realistic and healthy lifestyle modifications. By learning portion control, healthy food choices, and with the encouragement to get moving.
We would like the design to be gender neutral but must be fun.
The final design must be easy to use and useful to our clients.

Target Market(s)

Health, Wellbeing, Weightloss

Industry/Entity Type

Weight

Font styles to use
Sans Serif

Requirements
Must have
• Hydration log, Weigh-ins with fat %, Food log, Location of meetings,lectures and weigh-ins, list of restaurants that comply with B4J, Fitness plan, Mall walk maps, daily motivational message.

```html
<!DOCTYPE html>
<html lang="en">
<head>
<meta charset="utf-8">
<title>Hydration Log</title>
<link rel="stylesheet" href="https://fonts.googleapis.com/css2?family=Nunito+Sans:wght@300;400;600;700&display=swap">
<style>
  :root {
    --header-dark: #2b7bab;
    --header-light: #6fb3da;
    --tab-active: #3ccfa3;
    --tab-line: #a6d2ee;
    --white: #ffffff;
    --frame: #ececec;
    --ink: #3a3a3a;
    --muted: #9aa3a8;
    --water: #5faedc;
    --water-light: #a4dbf1;
    --oj: #4f8db0;
    --lemon: #2f86b6;
    --yoghurt: #2a8fc2;
    --cola: #1d6fa3;
    --tea: #155a8a;
    --sake: #0e4670;
    --label-mid: #4d9ec9;
    --label-dark: #1c5a86;
    --line: #cfd6da;
  }
  * { margin: 0; padding: 0; box-sizing: border-box; }
  html, body { width: 717px; height: 1200px; overflow: hidden; background: var(--white); }
  body { font-family: "Nunito Sans", Arial, sans-serif; color: var(--ink); }

  .screen { position: relative; width: 717px; height: 1200px; background: var(--frame); }

  .app-header {
    position: absolute; top: 0; left: 0; width: 717px; height: 144px;
    background: linear-gradient(100deg, var(--header-dark) 0%, #3a8cbe 40%, var(--header-light) 100%);
    color: var(--white);
  }
  .status-bar {
    position: absolute; top: 0; left: 0; right: 0; height: 46px;
    display: flex; align-items: center; justify-content: space-between;
    padding: 0 22px; font-size: 21px; font-weight: 400;
  }
  .status-left, .status-right { display: flex; align-items: center; gap: 8px; width: 220px; }
  .status-right { justify-content: flex-end; }
  .status-time { font-weight: 600; }

  .tabs { position: absolute; top: 60px; left: 0; right: 0; height: 80px; display: flex; }
  .tab { display: flex; align-items: center; gap: 14px; justify-content: center; opacity: .55; }
  .tab.is-active { opacity: 1; }
  .tab:nth-child(1) { width: 246px; }
  .tab:nth-child(2) { width: 235px; border-left: 1px solid rgba(255,255,255,.2); border-right: 1px solid rgba(255,255,255,.2); }
  .tab:nth-child(3) { width: 236px; }
  .tab-text { display: flex; flex-direction: column; align-items: center; line-height: 1; }
  .tab-kicker { font-size: 14px; letter-spacing: .3px; text-transform: uppercase; }
  .tab-title { font-size: 29px; font-weight: 300; margin-top: 4px; }

  .tab-indicator { position: absolute; bottom: 0; left: 0; right: 0; height: 5px; background: var(--tab-line); }
  .tab-indicator::before { content: ""; position: absolute; left: 0; top: 0; width: 246px; height: 5px; background: var(--tab-active); }

  .content {
    position: absolute; top: 144px; left: 8px; width: 701px; height: 1048px;
    background: var(--white);
  }
  .chart { position: absolute; top: -144px; left: -8px; width: 717px; height: 720px; }

  .label-pct { font-family: "Nunito Sans", Arial, sans-serif; font-weight: 700; font-size: 27px; }
  .label-name { font-family: "Nunito Sans", Arial, sans-serif; font-weight: 400; font-size: 14px; fill: var(--muted); }

  .summary { position: absolute; top: 625px; left: 0; right: 0; text-align: center; }
  .summary-title { font-size: 21px; font-weight: 400; letter-spacing: .5px; color: var(--ink); }
  .summary-value { margin-top: 14px; font-size: 58px; font-weight: 300; color: var(--water); }

  .ok-button {
    position: absolute; top: 915px; left: 257px; width: 187px; height: 60px;
    border: 2px solid #d6d6d6; border-radius: 30px; background: var(--white);
    font-family: inherit; font-size: 22px; font-weight: 700; color: #9b9b9b; letter-spacing: 1px;
  }
</style>
</head>
<body>
<main class="screen">
  <header class="app-header">
    <div class="status-bar">
      <div class="status-left">
        <svg width="68" height="12" viewBox="0 0 68 12" aria-hidden="true">
          <circle cx="6" cy="6" r="5" fill="#fff"/><circle cx="19" cy="6" r="5" fill="#fff"/><circle cx="32" cy="6" r="5" fill="#fff"/>
          <circle cx="45" cy="6" r="4.3" fill="none" stroke="#fff" stroke-width="1.3"/><circle cx="58" cy="6" r="4.3" fill="none" stroke="#fff" stroke-width="1.3"/>
        </svg>
        <span>NORTHWAVE</span>
        <svg width="22" height="16" viewBox="0 0 22 16" aria-hidden="true">
          <path d="M1 6a14 14 0 0 1 20 0" fill="none" stroke="#fff" stroke-width="2.4"/>
          <path d="M5 10a8.5 8.5 0 0 1 12 0" fill="none" stroke="#fff" stroke-width="2.4"/>
          <circle cx="11" cy="14" r="2" fill="#fff"/>
        </svg>
      </div>
      <div class="status-time">4:21 PM</div>
      <div class="status-right">
        <svg width="12" height="20" viewBox="0 0 12 20" aria-hidden="true">
          <path d="M1 5l10 9-5 4V2l5 4-10 9" fill="none" stroke="rgba(255,255,255,.7)" stroke-width="1.6"/>
        </svg>
        <span>100%</span>
        <svg width="44" height="20" viewBox="0 0 44 20" aria-hidden="true">
          <rect x="1" y="2" width="38" height="16" rx="3" fill="none" stroke="#fff" stroke-width="1.5"/>
          <rect x="3.5" y="4.5" width="33" height="11" rx="1.5" fill="#fff"/>
          <rect x="40.5" y="7" width="2.5" height="6" rx="1" fill="#fff"/>
        </svg>
      </div>
    </div>

    <nav class="tabs">
      <div class="tab is-active">
        <svg width="18" height="46" viewBox="0 0 18 46" aria-hidden="true">
          <circle cx="9" cy="5" r="4.5" fill="#fff"/>
          <rect x="2" y="11" width="14" height="18" rx="4" fill="#fff"/>
          <rect x="4" y="26" width="4" height="19" rx="2" fill="#fff"/>
          <rect x="10" y="26" width="4" height="19" rx="2" fill="#fff"/>
        </svg>
        <div class="tab-text"><span class="tab-kicker">Hydration</span><span class="tab-title">LOG</span></div>
      </div>
      <div class="tab">
        <svg width="26" height="34" viewBox="0 0 26 34" aria-hidden="true">
          <rect x="1" y="14" width="13" height="19" rx="2" fill="#fff"/>
          <rect x="4" y="6" width="7" height="8" fill="#fff"/>
          <rect x="15" y="20" width="10" height="13" rx="2" fill="#fff"/>
        </svg>
        <div class="tab-text"><span class="tab-kicker">Food</span><span class="tab-title">LOG</span></div>
      </div>
      <div class="tab">
        <svg width="24" height="30" viewBox="0 0 24 30" aria-hidden="true">
          <path d="M4 2h16v8a8 8 0 0 1-16 0z" fill="#fff"/>
          <rect x="10" y="17" width="4" height="7" fill="#fff"/>
          <rect x="6" y="24" width="12" height="4" rx="1" fill="#fff"/>
        </svg>
        <div class="tab-text"><span class="tab-kicker">Weigh in</span><span class="tab-title">FAT %</span></div>
      </div>
    </nav>
    <div class="tab-indicator"></div>
  </header>

  <section class="content">
    <svg class="chart" viewBox="0 0 717 720" role="img" aria-label="Hydration by drink: water 45%, orange juice 21%, lemonade 16%, yoghurt 12%, cola 9%, tea 6%, sake 2%">
      <defs>
        <linearGradient id="grad-water" x1="0.8" y1="0" x2="0.3" y2="0.6">
          <stop offset="0" stop-color="var(--water-light)"/>
          <stop offset="1" stop-color="var(--water)"/>
        </linearGradient>
        <linearGradient id="grad-oj" x1="0" y1="0" x2="1" y2="1">
          <stop offset="0" stop-color="#5e9cbd"/>
          <stop offset="1" stop-color="#4a86a8"/>
        </linearGradient>
        <linearGradient id="grad-lemon" x1="0" y1="0" x2="1" y2="1">
          <stop offset="0" stop-color="#2c6f9c"/>
          <stop offset="1" stop-color="#3aa0cf"/>
        </linearGradient>
        <linearGradient id="grad-yog" x1="0" y1="0" x2="1" y2="1">
          <stop offset="0" stop-color="#1f6b9a"/>
          <stop offset="1" stop-color="#32a3d4"/>
        </linearGradient>
      </defs>

      <path d="M360 430 L298.4 599.1 A180 180 0 0 1 360 250 Z" fill="url(#grad-water)"/>
      <path d="M360 430 L360 264 A166 166 0 0 1 526 430 Z" fill="url(#grad-oj)"/>
      <path d="M360 430 L504 430 A144 144 0 0 1 461.8 531.8 Z" fill="url(#grad-lemon)"/>
      <path d="M360 430 L457.6 527.6 A138 138 0 0 1 407.2 559.7 Z" fill="url(#grad-yog)"/>
      <path d="M360 430 L407.9 561.6 A140 140 0 0 1 364.9 569.9 Z" fill="var(--cola)"/>
      <path d="M360 430 L364.7 565.9 A136 136 0 0 1 336.4 563.9 Z" fill="var(--tea)"/>
      <path d="M360 430 L336.9 561.0 A133 133 0 0 1 314.5 555.0 Z" fill="var(--sake)"/>

      <g fill="none" stroke="var(--line)" stroke-width="1.2">
        <path d="M245 355 C200 350 190 310 198 288"/>
        <path d="M456 362 C500 340 515 310 506 268"/>
        <path d="M485 477 C510 505 540 510 565 496"/>
        <path d="M420 526 C440 550 470 560 503 548"/>
        <path d="M382 518 C392 560 410 585 440 590"/>
        <path d="M351 519 C340 560 345 590 352 600"/>
        <path d="M329 512 C310 560 280 600 250 608"/>
      </g>
      <g fill="#fff">
        <circle cx="245" cy="355" r="3.5"/>
        <circle cx="456" cy="362" r="3.5"/>
        <circle cx="485" cy="477" r="3.5"/>
        <circle cx="420" cy="526" r="3.5"/>
        <circle cx="382" cy="518" r="3.5"/>
        <circle cx="351" cy="519" r="3.5"/>
        <circle cx="329" cy="512" r="3.5"/>
      </g>

      <g text-anchor="middle">
        <text class="label-pct" x="144" y="310" fill="var(--water)">45%</text>
        <text class="label-name" x="144" y="328">Water</text>
        <text class="label-pct" x="507" y="250" fill="#6aa5c6">21%</text>
        <text class="label-name" x="507" y="268">Orange Juice</text>
        <text class="label-pct" x="573" y="454" fill="var(--label-mid)">16%</text>
        <text class="label-name" x="573" y="472">Lemonade</text>
        <text class="label-pct" x="529" y="554" fill="var(--lemon)">12%</text>
        <text class="label-name" x="529" y="572">Yoghurt</text>
        <text class="label-pct" x="440" y="621" fill="var(--label-dark)">9%</text>
        <text class="label-name" x="440" y="639">Fizz Cola</text>
        <text class="label-pct" x="353" y="645" fill="var(--label-dark)">6%</text>
        <text class="label-name" x="353" y="663">Tea</text>
        <text class="label-pct" x="234" y="648" fill="var(--sake)">2%</text>
        <text class="label-name" x="234" y="666">Sake</text>
      </g>
    </svg>

    <div class="summary">
      <p class="summary-title">TOTAL HYDRATION</p>
      <p class="summary-value">4,5 Liters</p>
    </div>

    <button class="ok-button" type="button">OK</button>
  </section>
</main>
</body>
</html>
```